Dental Medical History Form - Content provided

Design a medical history form for a dental practice. Content is provided so all that is needed is the formatting to make it look great and easy to read.

"Patient Information" to include all information contained in top portion of the "Patient Medical History Form" docx file.

"Medical History" should follow the formatting and content of the "Exact Medical History" file as this is what the entry fields look like in our practice software and so we would like it to match.

1st page - Patient info, allergies, medications, antibiotics, joint replacement, pregnancy.

2nd page - Do you have, or have you had, any of the following? . . . . . . .
Updates

Project Deadline Extended Reason: Picked too short of a deadline to start (2 days) Added Monday, February 13, 2017

Target Market(s)

All ages but must be clear enough for elderly to read. Use as much space as possible to keep font size bigger yet keep to two pages

Industry/Entity Type

Dental

Font styles to use
Sans Serif

Requirements
Must have
• All content provided
• Our logo at the top (file provided)
• Century Gothic Font
• Limit to two pages

```html
<!DOCTYPE html>
<html lang="en">
<head>
<meta charset="utf-8">
<title>Harbor Dental – Confidential Medical History</title>
<link href="https://fonts.googleapis.com/css2?family=Questrial&display=swap" rel="stylesheet">
<style>
  :root{
    --paper:#ffffff;
    --ink:#4a4a4a;
    --ink-soft:#6a6a6a;
    --ink-faint:#9a9a9a;
    --title:#5e534b;
    --rule:#a89a90;
    --field:#8a8a8a;
    --box:#7a7a7a;
  }
  *{box-sizing:border-box;margin:0;padding:0}
  html,body{width:1200px;height:832px;overflow:hidden;background:var(--paper)}
  body{position:relative;font-family:"Questrial","Century Gothic",sans-serif;color:var(--ink);font-size:9.8px}

  .page{position:absolute;top:0;height:832px}
  .page--front{left:89px;width:447px}
  .page--back{left:674px;width:438px}

  /* practice name */
  .practice-name{position:absolute;white-space:nowrap;color:var(--ink-soft);font-weight:400;line-height:1}
  .practice-name--header{left:0;top:92px;font-size:22px}
  .practice-name--footer{left:318px;top:564px;font-size:16px}

  .practice-address{position:absolute;right:0;top:81px;text-align:right;font-size:9.6px;line-height:11.7px;color:var(--ink-soft);font-style:normal}

  /* titled rules */
  .titled-rule{position:absolute;left:0;right:0;display:flex;align-items:center;gap:10px}
  .titled-rule::before,.titled-rule::after{content:"";flex:1;height:1.6px;background:var(--rule)}
  .titled-rule__text{font-size:10px;font-weight:700;letter-spacing:.3px;color:var(--title)}
  .titled-rule--front{top:134px}
  .titled-rule--front::before{flex:0 0 124px}
  .titled-rule--back{top:98px}
  .titled-rule--back::before{flex:0 0 102px}

  .divider{position:absolute;left:-6px;right:0;height:1.6px;background:var(--rule)}

  /* fields */
  .details{position:absolute;left:0;right:0;top:153px}
  .row{display:flex;align-items:flex-end;height:21.3px;gap:4px;white-space:nowrap}
  .line{flex:1;border-bottom:.8px solid var(--field);height:10px;position:relative}
  .line--short{flex:0 0 auto}
  .gap{width:8px}
  .sublabels{position:absolute;top:11px;left:0;right:0;font-size:5.6px;color:var(--ink-faint)}
  .sublabels span{position:absolute}
  .choice{display:inline-block}

  /* checkboxes */
  .check{display:flex;align-items:center;gap:11px;position:absolute;white-space:nowrap;line-height:1}
  .check--tight{gap:6px}
  .box{display:inline-block;width:11px;height:11px;border:.8px solid var(--box);flex:none}
  .two-line{line-height:.95;font-size:9.4px}

  .section-q{position:absolute;left:0;display:flex;align-items:center;gap:6px;font-size:10px}
  .write-line{position:absolute;height:0;border-bottom:.8px solid #b8b8b8}

  .yes-no{position:absolute;font-size:9.8px;white-space:nowrap}
  .turn-over{position:absolute;left:198px;top:749px;font-size:8.4px;font-weight:700;letter-spacing:.2px}

  /* back page */
  .prompt{position:absolute;left:0;right:0;top:116px;text-align:center;font-size:9.2px;font-weight:700;color:var(--ink)}
  .conditions{position:absolute;top:140px;display:flex;flex-direction:column}
  .conditions li{list-style:none;height:16.35px;display:flex;align-items:center;gap:6px;font-size:8.8px;white-space:nowrap;color:var(--ink-soft)}
  .conditions .group{font-weight:700;font-size:8px;color:var(--ink);padding-left:17px;letter-spacing:.2px}
  .conditions .box{width:10.5px;height:10.5px}
  .conditions .tiny{font-size:6.4px}
  .conditions .stack{font-size:8.2px;line-height:.85}
  .col-1{left:0}
  .col-2{left:173px}
  .col-3{left:318px}
  .describe{position:absolute;left:318px;width:120px;border-bottom:.8px solid #b8b8b8}
  .thanks{position:absolute;left:318px;top:452px;width:120px;font-size:8.4px;line-height:11.2px;color:var(--ink-soft)}
  .sign{position:absolute;left:-10px;right:0;top:727px;display:flex;align-items:flex-end;gap:5px;font-size:9.6px}
</style>
</head>
<body>

<section class="page page--front" aria-label="Confidential medical history, page 1">
  <div class="practice-name practice-name--header">Harbor Dental</div>
  <address class="practice-address">
    Harbor Dental<br>4.10/88 Coastal Parade<br>Ridgeway, NSW 2260<br>(02) 40 555 018
  </address>

  <div class="titled-rule titled-rule--front"><span class="titled-rule__text">CONFIDENTIAL MEDICAL HISTORY</span></div>

  <div class="details">
    <div class="row">Name: <span class="line"><span class="sublabels"><span style="left:12px">TITLE</span><span style="left:76px">FIRST</span><span style="left:172px">MIDDLE</span><span style="left:302px">LAST</span></span></span></div>
    <div class="row">Address: <span class="line"></span></div>
    <div class="row">DOB: <span class="line line--short" style="width:157px"></span><span class="gap"></span>E-Mail Address: <span class="line"></span></div>
    <div class="row">Phone Number(s): <span class="line"><span class="sublabels"><span style="left:45px">MOBILE</span><span style="left:142px">WORK</span><span style="left:237px">HOME</span></span></span></div>
    <div class="row">Emergency Contact Person: <span class="line"></span></div>
    <div class="row">Relationship: <span class="line line--short" style="width:188px"></span><span class="gap"></span>Phone Number: <span class="line"></span></div>
    <div class="row">General Practitioner Name: <span class="line"></span></div>
    <div class="row">Practice Name: <span class="line line--short" style="width:172px"></span><span class="gap"></span>Phone Number: <span class="line"></span></div>
    <div class="row">Do you have a health fund with dental coverage? <span class="choice" style="margin-left:36px">YES</span><span class="choice" style="margin-left:78px">NO</span></div>
    <div class="row">If yes, what is the name of the fund? <span class="line"></span></div>
    <div class="row">Fund Number: <span class="line line--short" style="width:144px"></span><span class="gap"></span>Priority Number on Card: <span class="choice" style="margin-left:14px;word-spacing:7px">0 1 2 3 4 5</span></div>
    <div class="row">Occupation: <span class="line line--short" style="width:148px"></span><span class="gap"></span>Referred By: <span class="line"></span></div>
  </div>

  <div class="divider" style="top:418px"></div>

  <div class="section-q" style="top:431px">Please indicate if you are allergic to any of the following: <span class="box"></span></div>
  <label class="check" style="left:10px;top:454px"><span class="box"></span>Aspirin</label>
  <label class="check" style="left:10px;top:470px"><span class="box"></span>Penicillin</label>
  <label class="check" style="left:10px;top:486px"><span class="box"></span>Latex</label>
  <label class="check" style="left:10px;top:503px"><span class="box"></span>Lactose</label>
  <label class="check check--tight" style="left:78px;top:454px"><span class="box"></span>Codeine</label>
  <label class="check check--tight" style="left:78px;top:470px"><span class="box"></span>Sulfites</label>
  <label class="check check--tight" style="left:78px;top:486px"><span class="box"></span>Local Anaesthetic</label>
  <label class="check check--tight" style="left:78px;top:503px"><span class="box"></span>Nickel</label>
  <div class="check" style="left:224px;top:455px">Other (please list):</div>
  <div class="write-line" style="left:317px;right:0;top:465px"></div>
  <div class="write-line" style="left:226px;right:0;top:481px"></div>
  <div class="write-line" style="left:226px;right:0;top:497px"></div>
  <div class="write-line" style="left:226px;right:0;top:513px"></div>

  <div class="divider" style="top:528px"></div>

  <div class="section-q" style="top:541px">Are you taking, or have you ever taken, any of the following medication(s): <span class="box"></span></div>
  <label class="check" style="left:10px;top:569px"><span class="box"></span>Asthma Inhaler</label>
  <label class="check" style="left:10px;top:585px"><span class="box"></span>Blood Thinners</label>
  <label class="check" style="left:10px;top:601px"><span class="box"></span><span class="two-line">Immuno-<br>suppressants</span></label>
  <label class="check check--tight" style="left:113px;top:569px"><span class="box"></span>Anti-epileptics</label>
  <label class="check check--tight" style="left:113px;top:585px"><span class="box"></span>Bisphosphates</label>
  <label class="check check--tight" style="left:113px;top:602px"><span class="box"></span>Steroids</label>
  <label class="check check--tight" style="left:210px;top:569px"><span class="box"></span>Anti-depressants</label>
  <label class="check check--tight" style="left:210px;top:585px"><span class="box"></span>Chemotherapy</label>
  <label class="check check--tight" style="left:210px;top:601px"><span class="box"></span><span class="two-line">Oral<br>contraceptives</span></label>
  <label class="check check--tight" style="left:317px;top:569px"><span class="box"></span>Blood Pressure</label>
  <label class="check check--tight" style="left:317px;top:585px"><span class="box"></span>Insulin</label>
  <label class="check check--tight" style="left:317px;top:602px"><span class="box"></span>Other</label>

  <div class="section-q" style="top:631px">Please specify any medications (name, dose, and frequency where possible)</div>
  <div class="write-line" style="left:0;width:210px;top:654px"></div>
  <div class="write-line" style="left:235px;right:0;top:654px"></div>
  <div class="write-line" style="left:0;width:210px;top:674px"></div>
  <div class="write-line" style="left:235px;right:0;top:674px"></div>
  <div class="write-line" style="left:0;width:210px;top:694px"></div>
  <div class="write-line" style="left:235px;right:0;top:694px"></div>

  <div class="yes-no" style="left:0;top:705px">Do you require antibiotic cover?&nbsp;&nbsp; Y&nbsp;&nbsp; N</div>
  <div class="yes-no" style="left:235px;top:705px">Have you had a joint replacement?&nbsp;&nbsp; Y&nbsp;&nbsp; N</div>
  <div class="yes-no" style="left:0;top:722px">Women: <span style="margin-left:20px">Are you pregnant?&nbsp;&nbsp; Y&nbsp;&nbsp; N</span></div>
  <div class="yes-no" style="left:235px;top:722px">Breast Feeding?&nbsp;&nbsp; Y&nbsp;&nbsp; N</div>

  <div class="turn-over">PLEASE TURN OVER</div>
</section>

<section class="page page--back" aria-label="Confidential medical history, page 2">
  <div class="titled-rule titled-rule--back" style="left:6px"><span class="titled-rule__text">CONFIDENTIAL MEDICAL HISTORY - PAGE 2</span></div>
  <p class="prompt">Do you have, or have you had, any of the following?</p>

  <ul class="conditions col-1">
    <li class="group">DENTAL:</li>
    <li><span class="box"></span>Acid Reflux</li>
    <li><span class="box"></span>Bad Breath/Taste</li>
    <li><span class="box"></span>Bleeding/Swollen/Sore Gums</li>
    <li><span class="box"></span>Blisters/Ulcers in Mouth</li>
    <li><span class="box"></span>Broken Tooth/Filling</li>
    <li><span class="box"></span>Burning Tongue</li>
    <li><span class="box"></span>Dry Mouth</li>
    <li><span class="box"></span>Food Collection Between Teeth</li>
    <li><span class="box"></span>Grinding/Clenching Teeth<span class="tiny">(day/night)</span></li>
    <li><span class="box"></span>Loose Teeth</li>
    <li><span class="box"></span>Crooked Teeth</li>
    <li><span class="box"></span>Discoloured Teeth</li>
    <li><span class="box"></span>Sensitivity to Hot/Cold</li>
    <li><span class="box"></span>Tooth Pain When Chewing</li>
    <li><span class="box"></span>Jaw Pain/Fracture</li>
    <li><span class="box"></span>Orthodontic Treatment</li>
    <li><span class="box"></span>Oral Cancer</li>
    <li class="group">DIET/LIFESTYLE:</li>
    <li><span class="box"></span><span class="stack">Drink More than One Glass<br>of Alcohol/Day</span></li>
    <li><span class="box"></span>Smoking</li>
    <li><span class="box"></span>Carbonated Drinks</li>
    <li><span class="box"></span>Sugary Foods</li>
    <li class="group">BLOOD:</li>
    <li><span class="box"></span>Anaemia</li>
    <li><span class="box"></span>Blood Clots</li>
    <li><span class="box"></span>Leukemia</li>
    <li><span class="box"></span>Low Platelets</li>
    <li><span class="box"></span>Lymphoma</li>
    <li><span class="box"></span>Haemophelia</li>
    <li class="group">CHEST:</li>
    <li><span class="box"></span>Bronchitis</li>
    <li><span class="box"></span>Cystic Fibrosis</li>
    <li><span class="box"></span>Emphysema</li>
    <li><span class="box"></span>Pneumonia</li>
  </ul>

  <ul class="conditions col-2">
    <li class="group">INFECTIOUS DISEASE:</li>
    <li><span class="box"></span>Creutzfeldt Jakob Disease</li>
    <li><span class="box"></span>Hepatitis A/B/C/D</li>
    <li><span class="box"></span>HIV/AIDS</li>
    <li><span class="box"></span>Shingles</li>
    <li><span class="box"></span>Influenza</li>
    <li><span class="box"></span>Tuberculosis</li>
    <li class="group">HEART</li>
    <li><span class="box"></span>Angina</li>
    <li><span class="box"></span>Atrial Fibrillation</li>
    <li><span class="box"></span>Blood Pressure</li>
    <li><span class="box"></span>Congenital Heart Disease</li>
    <li><span class="box"></span>Heart Attack</li>
    <li><span class="box"></span>Heart Murmur</li>
    <li><span class="box"></span>Heart Surgery</li>
    <li><span class="box"></span>Heart Valve Replacement</li>
    <li><span class="box"></span>Infective Endorcarditis</li>
    <li><span class="box"></span>Rheumatic Heart Disease</li>
    <li><span class="box"></span>Pacemaker</li>
    <li><span class="box"></span>Stent</li>
    <li class="group">OTHER</li>
    <li><span class="box"></span>Anxiety/PTSD</li>
    <li><span class="box"></span>Arthritis</li>
    <li><span class="box"></span>Alzheimer's</li>
    <li><span class="box"></span>Asthma</li>
    <li><span class="box"></span>Anaphylaxis</li>
    <li><span class="box"></span>Auto-Immune Disease</li>
    <li><span class="box"></span>Coeliac</li>
    <li><span class="box"></span>Depression</li>
    <li><span class="box"></span>Diabetes</li>
    <li><span class="box"></span>Epilepsy</li>
    <li><span class="box"></span>Kidney Disease</li>
  </ul>

  <ul class="conditions col-3">
    <li><span class="box"></span>Liver Disease</li>
    <li><span class="box"></span>Osteoporosis</li>
    <li><span class="box"></span>Parkinson's</li>
    <li><span class="box"></span>Radiation to Head/Neck</li>
    <li><span class="box"></span>Schizophrenia</li>
    <li><span class="box"></span>Snoring</li>
    <li><span class="box"></span>Sleep Apnea</li>
    <li><span class="box"></span>Stroke</li>
    <li><span class="box"></span>Other (describe below)</li>
  </ul>
  <div class="describe" style="top:314px"></div>
  <div class="describe" style="top:330px"></div>
  <div class="describe" style="top:347px"></div>
  <div class="describe" style="top:363px"></div>

  <p class="thanks">Thank you for taking the time to complete your medical history form. Oral health is linked to overall health and this comprehensive questionnaire will help us to provide you with optimal and safe care.</p>

  <div class="practice-name practice-name--footer">Harbor Dental</div>

  <div class="sign">Signature: <span class="line" style="flex:0 0 212px"></span><span class="gap"></span>Date: <span class="line"></span></div>
</section>

</body>
</html>
```